Greek God inspired Air Freshen needs Foil Package Design

We are Hall of Zephyra. We sell car air fresheners inspired by Ancient Greece. We currently sell 5 proprietary scents. You can see them here: https://www.shopvendra.com/Freshener-Natural-Essential-Hall-Zephyra/dp/K7R2QQWN4M
These are luxury air fresheners sold in awesome packages. 100% essential oils blended and bottled in the USA.
We need your help! We want to sell an additional line of scents. This line will be called "The Lyra Series" - or, The Lyra Series by Hall of Zephyra. This collection's theme will be - "The aromas you love, refined on high."
These new products will be takes on well know colognes and perfumes.
We will start with 3 new products:
Talvor – inspired by Brimara by Vask
Menthile – inspired by Ferolin by Lune
Pelion – inspired by Ombra by Tessin
Our original 5 products are packaged in tubes and bottled in a luxury black 8ml bottle (see attached and the link above). The "Lyra Series" will also have the same bottles, BUT, we want to package them in MYLAR FOIL BAGS. They will be 10x7cm (template attached).
What we need from you guys .... 3 designs. Front of the bag ONLY. One for each:
You have free reign, however the following items must be met:
The designs must be min 300 dpi.
Must include: "Lyra Series by Hall of Zephyra"
Must include: Hall of Zephyra Logo (attached)
Must include the words: "Car Air Fresheners"
Must marry well with our current imagery: https://www.shopvendra.com/Freshener-Natural-Essential-Hall-Zephyra/dp/K7R2QQWN4M
Don't necessarily need to mention the cologne that our product is inspired by, however, perhaps consider use some fonts/pattern/s shadows of the Vask/Brimara bottle "shape" as an example.
Keep in mind, you are only designing the front of the packages. We will complete the back. The back will have the brand story, instructions, UPC, ingredients.
Our thoughts on using foil mylar bags: 1. We sell online 2. They will stand out from the others 3. Gives you/designer more space/opportunity to convey the product/message 4. We believe mock-ups/photos of the bags will look great on our listing
Please contact with any questions.

```html
<!DOCTYPE html>
<html lang="en">
<head>
<meta charset="utf-8">
<title>Hall of Zephyra — The Lyra Series Pouches</title>
<link href="https://fonts.googleapis.com/css2?family=Old+Standard+TT:wght@400&family=Saira+Semi+Condensed:wght@600&display=swap" rel="stylesheet">
<style>
  :root {
    --paper: #f6f6f6;
    --pouch: #050505;
    --gold: #c9a23a;
    --gold-light: #e2c25c;
    --gold-dark: #8f6f1c;
    --ink-dark: #1a1206;
  }
  html, body {
    margin: 0;
    padding: 0;
    width: 1200px;
    height: 849px;
    overflow: hidden;
    background: var(--paper);
  }
  .canvas {
    position: relative;
    width: 1200px;
    height: 849px;
  }
  .pouch {
    position: absolute;
    top: 227px;
    width: 312px;
    height: 408px;
    background: var(--pouch);
    text-align: center;
  }
  .pouch--talvor { left: 55px; }
  .pouch--pelion { left: 440px; }
  .pouch--menthile { left: 825px; }

  .pouch__art {
    position: absolute;
    top: 0;
    left: 24px;
    width: 262px;
    height: 166px;
  }
  .pouch__art::after {
    content: "";
    position: absolute;
    inset: 0;
    background: linear-gradient(to bottom, rgba(5,5,5,0) 60%, var(--pouch) 100%);
  }
  .pouch--talvor .pouch__art {
    background: linear-gradient(120deg, #1f3b45 0%, #4a3a2a 50%, #b06a30 100%);
  }
  .pouch--pelion .pouch__art {
    background: linear-gradient(180deg, #d9b45a 0%, #2f9aa6 60%, #123d4c 100%);
  }
  .pouch--menthile .pouch__art {
    background: linear-gradient(180deg, #1c2638 0%, #4a5568 60%, #2a3242 100%);
  }

  .pouch__mark {
    position: absolute;
    top: 168px;
    left: 50%;
    transform: translateX(-50%);
  }
  .pouch__brand {
    position: absolute;
    top: 229px;
    left: 0;
    right: 0;
    font-family: "Saira Semi Condensed", sans-serif;
    font-weight: 600;
    font-size: 9px;
    line-height: 1;
    letter-spacing: 0.3px;
    color: var(--gold);
  }
  .pouch__name {
    position: absolute;
    top: 241px;
    left: 0;
    right: 0;
    margin: 0;
    font-family: "Old Standard TT", serif;
    font-weight: 400;
    font-size: 37px;
    line-height: 1;
    letter-spacing: 2px;
    color: var(--gold);
  }
  .pouch__series {
    position: absolute;
    top: 282px;
    left: 0;
    right: 0;
    font-family: "Old Standard TT", serif;
    font-size: 11.5px;
    line-height: 1;
    letter-spacing: 2.6px;
    color: var(--gold);
  }
  .pouch__label {
    position: absolute;
    top: 306px;
    left: 50%;
    transform: translateX(-50%);
    width: 139px;
    height: 47px;
    box-sizing: border-box;
    background: linear-gradient(90deg, var(--gold-dark), var(--gold-light) 50%, var(--gold-dark));
    border: 1px solid var(--gold-light);
    outline: 1px solid var(--gold-dark);
    outline-offset: -4px;
    display: flex;
    align-items: center;
    justify-content: center;
    font-family: "Old Standard TT", serif;
    font-size: 15px;
    line-height: 1.1;
    letter-spacing: 1.6px;
    color: var(--ink-dark);
  }
  .pouch__band {
    position: absolute;
    top: 364px;
    left: 50%;
    transform: translateX(-50%);
    width: 240px;
    height: 20px;
    background: linear-gradient(90deg, var(--gold-dark), var(--gold-light) 50%, var(--gold-dark));
  }
</style>
</head>
<body>
<main class="canvas">

  <section class="pouch pouch--talvor">
    <div class="pouch__art" role="img" aria-label="Scent artwork area in teal and amber tones"></div>
    <svg class="pouch__mark" width="48" height="48" viewBox="0 0 48 48" aria-hidden="true">
      <circle cx="24" cy="24" r="20" fill="none" stroke="#c9a23a" stroke-width="2"/>
    </svg>
    <div class="pouch__brand">HALL OF ZEPHYRA</div>
    <h2 class="pouch__name">TALVOR</h2>
    <div class="pouch__series">THE LYRA SERIES</div>
    <div class="pouch__label">CAR AIR<br>FRESHENERS</div>
    <div class="pouch__band"></div>
  </section>

  <section class="pouch pouch--pelion">
    <div class="pouch__art" role="img" aria-label="Scent artwork area in gold and turquoise tones"></div>
    <svg class="pouch__mark" width="48" height="48" viewBox="0 0 48 48" aria-hidden="true">
      <circle cx="24" cy="24" r="20" fill="none" stroke="#c9a23a" stroke-width="2"/>
    </svg>
    <div class="pouch__brand">HALL OF ZEPHYRA</div>
    <h2 class="pouch__name">PELION</h2>
    <div class="pouch__series">THE LYRA SERIES</div>
    <div class="pouch__label">CAR AIR<br>FRESHENERS</div>
    <div class="pouch__band"></div>
  </section>

  <section class="pouch pouch--menthile">
    <div class="pouch__art" role="img" aria-label="Scent artwork area in slate and night blue tones"></div>
    <svg class="pouch__mark" width="48" height="48" viewBox="0 0 48 48" aria-hidden="true">
      <circle cx="24" cy="24" r="20" fill="none" stroke="#c9a23a" stroke-width="2"/>
    </svg>
    <div class="pouch__brand">HALL OF ZEPHYRA</div>
    <h2 class="pouch__name">MENTHILE</h2>
    <div class="pouch__series">THE LYRA SERIES</div>
    <div class="pouch__label">CAR AIR<br>FRESHENERS</div>
    <div class="pouch__band"></div>
  </section>

</main>
</body>
</html>
```